E-Commerce Website Update for Bamboo Poles Company

Existing website at:

http://www.reedcraftstudio.example/
http://www.reedcraftstudio.example/pages/product-and-price-list

Two pages to design: home page and "price list" page.

Info for home page as follows:

HOME PAGE:

Header:
Company Name: reedcraft studio
Telephone: 1 888 412 5093

Across the top:
Home | Price List | Blog | FAQ | About | Contact

Down the side:
About Bamboo
Wedding Arbors
Bamboo For Flutes
Black Bamboo
Spotted Bamboo
Bamboo Carpentry
Photo Gallery
All Products & Prices
Blog
FAQ
About
Contact

Should have shopping cart and search buttons on top.
Please see ai file, attached for logo (leaf) and font
In addition the homepage should have one or two sections for promotions

Chosen design will be asked to help deign a PRODUCT AND PRICE LIST page similar to the one we have now, but with "LEARN MORE" and "ORDER NOW" buttons for each item.
Updates

Reason: Thanks  for all the designs so far; giving an extra week for extra consideration.

Target Market(s)

Consumers, wedding planners.

Industry/Entity Type

Shopping

Requirements
Must have
• Clean, easy to read design.
Should not have
• No flash animation.

```html
<!DOCTYPE html>
<html lang="en">
<head>
<meta charset="utf-8">
<title>reedcraft studio — All Products</title>
<link rel="stylesheet" href="https://fonts.googleapis.com/css2?family=Open+Sans:wght@400;600&family=Noto+Serif:wght@400&display=swap">
<style>
:root{
  --band:#1b1b1b;
  --green:#7cc242;
  --green-light:#a9db7c;
  --green-dark:#5f9a2a;
  --green-text:#5a8e1c;
  --sidebar:#f2f2f2;
  --card:#f1f1f1;
  --card-edge:#dcdcdc;
  --text:#222;
  --muted:#444;
  --white:#fff;
}
*{box-sizing:border-box;margin:0;padding:0}
html,body{width:1200px;height:1200px;overflow:hidden;background:var(--white)}
body{position:relative;font-family:"Open Sans",sans-serif;color:var(--text)}

.site-header{position:absolute;left:0;top:0;width:1200px;height:110px;background:linear-gradient(#121212 0%,#161616 60%,#262626 100%)}
.header-rule{position:absolute;left:0;top:108px;width:1200px;height:6px;background:var(--green)}
.brand{position:absolute;left:47px;top:14px;display:flex;align-items:center;gap:14px}
.brand-mark{width:28px;height:28px;border-radius:50%;background:var(--green)}
.brand-name{font-size:34px;font-weight:400;color:var(--white);line-height:1}
.phone{position:absolute;left:132px;top:70px;font-size:20px;color:var(--white)}

.cart{position:absolute;left:752px;top:8px;display:flex;gap:10px;align-items:flex-start}
.cart-text{font-family:"Noto Serif",serif;font-size:13.5px;line-height:17px;color:var(--green);width:145px}
.divider{position:absolute;left:950px;top:6px;width:1px;height:36px;background:#3a3a3a}
.search{position:absolute;left:965px;top:11px;width:186px;height:21px;border-radius:11px;background:var(--white);border:1px solid #999;display:flex;align-items:center;padding-left:7px;gap:4px;font-size:12px;color:#111}

.main-nav{position:absolute;left:565px;top:86px;display:flex;gap:7px}
.main-nav a{display:block;width:85px;height:22px;background:var(--green);color:var(--white);text-decoration:none;font-size:15px;text-align:center;line-height:22px;border-radius:6px 10px 0 0;clip-path:polygon(0 0,88% 0,100% 100%,0 100%)}
.main-nav a.active{background:var(--green-light)}

.page-title{position:absolute;left:50px;top:151px;font-size:28px;font-weight:400;color:#333}

.product-grid{position:absolute;left:47px;top:188px;display:grid;grid-template-columns:repeat(5,130px);column-gap:25px;row-gap:29px}
.product{width:130px;height:257px;background:var(--card);border:1px solid var(--card-edge);padding:4px}
.product-photo{width:120px;height:160px;background:linear-gradient(90deg,#ddd 0%,#ddd 4%,#c9b47c 6%,#d8c48c 22%,#c4ac6c 42%,#b9a066 47%,#d2bd84 55%,#c6ad6e 78%,#d8d6d2 83%,#e0e0e0 100%)}
.product-name{font-size:13px;line-height:16px;color:var(--green-text);padding:5px 3px 3px;border-bottom:1px solid #e3e3e3;white-space:nowrap}
.product-price{font-size:13px;line-height:16px;padding:4px 3px 5px;color:#111}
.product-actions{display:flex;gap:4px}
.product-actions a{flex:1;height:20px;line-height:20px;text-align:center;font-size:10.5px;font-weight:600;color:var(--white);text-decoration:none;border-radius:2px;white-space:nowrap}
.btn-learn{background:linear-gradient(#555,#2a2a2a)}
.btn-order{background:linear-gradient(var(--green),var(--green-dark))}

.pager{position:absolute;left:50px;top:1042px;display:flex;gap:7px}
.pager a{display:block;height:21px;line-height:21px;background:linear-gradient(#555,#2a2a2a);color:var(--white);font-size:13.5px;text-decoration:none;border-radius:2px;text-align:center}
.pager a.step{width:52px}
.pager a.num{width:22px}
.content-rule{position:absolute;left:50px;top:1075px;width:750px;height:2px;background:linear-gradient(90deg,var(--green) 0,var(--green) 55px,#9aa78a 60px,#9aa78a 100%)}

.sidebar{position:absolute;left:810px;top:150px;width:343px;height:942px;background:var(--sidebar);border:1px solid #e6e6e6}
.side-nav{list-style:none;padding:20px 16px 0;display:flex;flex-direction:column;gap:8px}
.side-nav li{border-bottom:1px solid #dedede}
.side-nav a{font-family:"Noto Serif",serif;font-size:20px;color:var(--muted);text-decoration:none;line-height:26px}

.site-footer{position:absolute;left:0;top:1108px;width:1200px;height:92px;background:linear-gradient(#111 0%,#151515 55%,#2a2a2a 100%)}
.footer-brand{position:absolute;left:47px;top:22px;display:flex;align-items:center;gap:10px}
.footer-brand .brand-mark{width:22px;height:22px}
.footer-brand .brand-name{font-size:27px}
.footer-nav{position:absolute;top:6px;left:0;width:1200px}
.footer-nav a{position:absolute;color:var(--white);text-decoration:none;font-size:16px}
</style>
</head>
<body>

<header class="site-header">
  <div class="brand">
    <span class="brand-mark"></span>
    <span class="brand-name">reedcraft studio</span>
  </div>
  <div class="phone">1 888 412 5093</div>

  <div class="cart">
    <svg width="38" height="28" viewBox="0 0 38 28" aria-hidden="true">
      <path d="M1 3h7l5 15h18l4-11H11" fill="none" stroke="#7cc242" stroke-width="3" stroke-linejoin="round"/>
      <rect x="12" y="8" width="21" height="8" fill="#7cc242"/>
      <circle cx="15" cy="24" r="3" fill="#7cc242"/>
      <circle cx="29" cy="24" r="3" fill="#7cc242"/>
    </svg>
    <div class="cart-text">Your Cart is currently empty.</div>
  </div>
  <div class="divider"></div>
  <div class="search">
    <svg width="18" height="12" viewBox="0 0 18 12" aria-hidden="true">
      <circle cx="5" cy="5" r="3.5" fill="none" stroke="#333" stroke-width="1.6"/>
      <line x1="7.5" y1="7.5" x2="10.5" y2="10.5" stroke="#333" stroke-width="1.8"/>
      <path d="M12 4l2.5 3 2.5-3z" fill="#333"/>
    </svg>
    Search
  </div>

  <nav class="main-nav">
    <a class="active" href="#">home</a>
    <a href="#">price list</a>
    <a href="#">blog</a>
    <a href="#">FAQ</a>
    <a href="#">about</a>
    <a href="#">contact</a>
  </nav>
</header>
<div class="header-rule"></div>

<h1 class="page-title">All Products</h1>

<section class="product-grid">
  <article class="product"><div class="product-photo" role="img" aria-label="Two spotted bamboo poles"></div><div class="product-name">1 7/8" x 8 feet<br>Spotted Bamboo</div><div class="product-price">$28.00</div><div class="product-actions"><a class="btn-learn" href="#">Learn More</a><a class="btn-order" href="#">Order Now</a></div></article>
  <article class="product"><div class="product-photo" role="img" aria-label="Two spotted bamboo poles"></div><div class="product-name">1 7/8" x 8 feet<br>Spotted Bamboo</div><div class="product-price">$28.00</div><div class="product-actions"><a class="btn-learn" href="#">Learn More</a><a class="btn-order" href="#">Order Now</a></div></article>
  <article class="product"><div class="product-photo" role="img" aria-label="Two spotted bamboo poles"></div><div class="product-name">1 7/8" x 8 feet<br>Spotted Bamboo</div><div class="product-price">$28.00</div><div class="product-actions"><a class="btn-learn" href="#">Learn More</a><a class="btn-order" href="#">Order Now</a></div></article>
  <article class="product"><div class="product-photo" role="img" aria-label="Two spotted bamboo poles"></div><div class="product-name">1 7/8" x 8 feet<br>Spotted Bamboo</div><div class="product-price">$28.00</div><div class="product-actions"><a class="btn-learn" href="#">Learn More</a><a class="btn-order" href="#">Order Now</a></div></article>
  <article class="product"><div class="product-photo" role="img" aria-label="Two spotted bamboo poles"></div><div class="product-name">1 7/8" x 8 feet<br>Spotted Bamboo</div><div class="product-price">$28.00</div><div class="product-actions"><a class="btn-learn" href="#">Learn More</a><a class="btn-order" href="#">Order Now</a></div></article>
  <article class="product"><div class="product-photo" role="img" aria-label="Two spotted bamboo poles"></div><div class="product-name">1 7/8" x 8 feet<br>Spotted Bamboo</div><div class="product-price">$28.00</div><div class="product-actions"><a class="btn-learn" href="#">Learn More</a><a class="btn-order" href="#">Order Now</a></div></article>
  <article class="product"><div class="product-photo" role="img" aria-label="Two spotted bamboo poles"></div><div class="product-name">1 7/8" x 8 feet<br>Spotted Bamboo</div><div class="product-price">$28.00</div><div class="product-actions"><a class="btn-learn" href="#">Learn More</a><a class="btn-order" href="#">Order Now</a></div></article>
  <article class="product"><div class="product-photo" role="img" aria-label="Two spotted bamboo poles"></div><div class="product-name">1 7/8" x 8 feet<br>Spotted Bamboo</div><div class="product-price">$28.00</div><div class="product-actions"><a class="btn-learn" href="#">Learn More</a><a class="btn-order" href="#">Order Now</a></div></article>
  <article class="product"><div class="product-photo" role="img" aria-label="Two spotted bamboo poles"></div><div class="product-name">1 7/8" x 8 feet<br>Spotted Bamboo</div><div class="product-price">$28.00</div><div class="product-actions"><a class="btn-learn" href="#">Learn More</a><a class="btn-order" href="#">Order Now</a></div></article>
  <article class="product"><div class="product-photo" role="img" aria-label="Two spotted bamboo poles"></div><div class="product-name">1 7/8" x 8 feet<br>Spotted Bamboo</div><div class="product-price">$28.00</div><div class="product-actions"><a class="btn-learn" href="#">Learn More</a><a class="btn-order" href="#">Order Now</a></div></article>
  <article class="product"><div class="product-photo" role="img" aria-label="Two spotted bamboo poles"></div><div class="product-name">1 7/8" x 8 feet<br>Spotted Bamboo</div><div class="product-price">$28.00</div><div class="product-actions"><a class="btn-learn" href="#">Learn More</a><a class="btn-order" href="#">Order Now</a></div></article>
  <article class="product"><div class="product-photo" role="img" aria-label="Two spotted bamboo poles"></div><div class="product-name">1 7/8" x 8 feet<br>Spotted Bamboo</div><div class="product-price">$28.00</div><div class="product-actions"><a class="btn-learn" href="#">Learn More</a><a class="btn-order" href="#">Order Now</a></div></article>
  <article class="product"><div class="product-photo" role="img" aria-label="Two spotted bamboo poles"></div><div class="product-name">1 7/8" x 8 feet<br>Spotted Bamboo</div><div class="product-price">$28.00</div><div class="product-actions"><a class="btn-learn" href="#">Learn More</a><a class="btn-order" href="#">Order Now</a></div></article>
  <article class="product"><div class="product-photo" role="img" aria-label="Two spotted bamboo poles"></div><div class="product-name">1 7/8" x 8 feet<br>Spotted Bamboo</div><div class="product-price">$28.00</div><div class="product-actions"><a class="btn-learn" href="#">Learn More</a><a class="btn-order" href="#">Order Now</a></div></article>
  <article class="product"><div class="product-photo" role="img" aria-label="Two spotted bamboo poles"></div><div class="product-name">1 7/8" x 8 feet<br>Spotted Bamboo</div><div class="product-price">$28.00</div><div class="product-actions"><a class="btn-learn" href="#">Learn More</a><a class="btn-order" href="#">Order Now</a></div></article>
</section>

<nav class="pager">
  <a class="step" href="#">Back</a>
  <a class="num" href="#">1</a>
  <a class="num" href="#">2</a>
  <a class="num" href="#">3</a>
  <a class="num" href="#">4</a>
  <a class="step" href="#">Next</a>
</nav>
<div class="content-rule"></div>

<aside class="sidebar">
  <ul class="side-nav">
    <li><a href="#">About Bamboo</a></li>
    <li><a href="#">Wedding Arbors</a></li>
    <li><a href="#">Bamboo For Flutes</a></li>
    <li><a href="#">Black Bamboo</a></li>
    <li><a href="#">Spotted Bamboo</a></li>
    <li><a href="#">Bamboo Carpentry</a></li>
    <li><a href="#">Photo Gallery</a></li>
    <li><a href="#">All Products &amp; Prices</a></li>
    <li><a href="#">Blog</a></li>
    <li><a href="#">FAQ</a></li>
    <li><a href="#">About</a></li>
    <li><a href="#">Contact</a></li>
  </ul>
</aside>

<footer class="site-footer">
  <div class="footer-brand">
    <span class="brand-mark"></span>
    <span class="brand-name">reedcraft studio</span>
  </div>
  <nav class="footer-nav">
    <a href="#" style="left:648px">home</a>
    <a href="#" style="left:730px">price list</a>
    <a href="#" style="left:836px">blog</a>
    <a href="#" style="left:928px">FAQ</a>
    <a href="#" style="left:1013px">about</a>
    <a href="#" style="left:1099px">contact</a>
  </nav>
</footer>

</body>
</html>
```